I am looking for a stand-out cover that sings out to new parents. The category is very pastel with limited compelling covers that would make me want to buy a book. This book will be used often in the first 12 months of baby's life - so must be strong enough to sit on the bedside table or on the coffee table to inspire reading. It will be a popular gift - so needs to look credible, "pick-up-able" and loveable.

The Book Title is - The Cradle Compass to Infancy's Opening Seasons: Grounded, Research-Led Methods on Rest, Nourishment, Protection plus Growing Assurance
The Size is - 8.5 x 11 in
Book description to be provided to final design for inclusion
Some examples of book covers in this category attached. Thanks

```html
<!DOCTYPE html>
<html lang="en">
<head>
<meta charset="utf-8">
<title>The Cradle Compass to Infancy's Opening Seasons – Cover</title>
<link rel="stylesheet" href="https://fonts.googleapis.com/css2?family=Oswald:wght@300;400;700&family=Poppins:wght@400&display=swap">
<style>
  :root {
    --teal: #2b92a6;
    --teal-soft: #5fa9b8;
    --sun: #f2c865;
    --coral: #f07d7a;
    --blush: #f9d6d4;
    --white: #ffffff;
    --page: #f4f4f4;
    --linen: #eef0ef;
    --hair: #7a5a3c;
    --skin: #e9c2a8;
    --skin-light: #f3dccd;
  }
  * { margin: 0; padding: 0; box-sizing: border-box; }
  html, body { width: 1200px; height: 574px; overflow: hidden; background: var(--page); }
  .stage { position: relative; width: 1200px; height: 574px; }

  .cover {
    position: absolute; left: 406px; top: 36px; width: 388px; height: 502px;
    background: var(--teal); overflow: hidden;
    box-shadow: 0 6px 18px rgba(0,0,0,.18);
  }
  .cover__band {
    position: absolute; top: 0; bottom: 0; width: 20px; z-index: 2;
    background: linear-gradient(to bottom, var(--white) 0%, var(--white) 58%, var(--blush) 72%, var(--coral) 100%);
  }
  .cover__band::after {
    content: ""; position: absolute; top: 0; bottom: 0; width: 4px;
    background: rgba(0,0,0,.06);
  }
  .cover__band--left { left: 0; }
  .cover__band--left::after { left: 8px; }
  .cover__band--right { right: 0; }
  .cover__band--right::after { right: 8px; }

  .cover__photo {
    position: absolute; left: 20px; right: 20px; top: 280px; bottom: 0;
    background:
      radial-gradient(ellipse 34% 30% at 44% 70%, var(--skin-light) 0%, rgba(243,220,205,.85) 45%, rgba(243,220,205,0) 100%),
      radial-gradient(ellipse 30% 26% at 64% 46%, var(--skin) 0%, rgba(233,194,168,.8) 45%, rgba(233,194,168,0) 100%),
      radial-gradient(ellipse 52% 44% at 62% 46%, var(--hair) 0%, rgba(122,90,60,.7) 40%, rgba(122,90,60,0) 100%),
      radial-gradient(ellipse 40% 30% at 82% 66%, rgba(255,255,255,.9) 0%, rgba(255,255,255,0) 100%),
      linear-gradient(to bottom, var(--teal) 0%, var(--teal-soft) 12%, #a9c9cf 32%, #dfe6e6 62%, var(--linen) 100%);
  }

  .glow { position: absolute; border-radius: 50%; filter: blur(3px); }
  .glow--sun { left: 58px; top: 118px; width: 14px; height: 14px; background: var(--sun); opacity: .85; }
  .glow--coral { left: 304px; top: 112px; width: 24px; height: 24px; background: var(--coral); opacity: .85; }

  .title { position: absolute; left: 20px; right: 20px; top: 24px; text-align: center; font-family: "Oswald", sans-serif; }
  .title__kicker {
    display: block; color: var(--white); font-weight: 300; font-size: 18px;
    letter-spacing: 13px; line-height: 1; padding-left: 13px;
  }
  .title__hero {
    display: block; color: var(--sun); font-weight: 700; font-size: 64px;
    line-height: .95; margin-top: -2px; letter-spacing: -1px;
  }
  .title__link {
    display: block; color: var(--white); font-weight: 400; font-size: 22px;
    line-height: 1; margin-top: 6px; transform: scaleX(.88);
  }
  .title__closing { display: block; margin-top: 4px; line-height: 1; }
  .title__closing-main { color: var(--sun); font-weight: 700; font-size: 50px; letter-spacing: -.5px; }
  .title__closing-tail { color: var(--white); font-weight: 400; font-size: 21px; margin-left: 4px; }

  .subtitle {
    position: absolute; left: 46px; right: 46px; top: 207px; text-align: center;
    color: var(--white); font-family: "Poppins", sans-serif; font-size: 10px; line-height: 1.4;
  }

  .topics { position: absolute; top: 252px; left: 0; right: 0; height: 50px; z-index: 1; }
  .topic {
    position: absolute; top: 0; width: 50px; height: 50px; border-radius: 50%;
    display: flex; align-items: center; justify-content: center;
  }
  .topic svg { width: 28px; height: 28px; fill: none; stroke-width: 1.6; stroke-linecap: round; stroke-linejoin: round; }
  .topic--safety { left: 95px; background: var(--white); }
  .topic--safety svg { stroke: var(--teal); }
  .topic--feeding { left: 169px; background: var(--sun); }
  .topic--feeding svg { stroke: var(--white); }
  .topic--sleep { left: 244px; background: var(--coral); }
  .topic--sleep svg { stroke: var(--white); }
</style>
</head>
<body>
<main class="stage">
  <article class="cover">
    <div class="cover__photo" role="img" aria-label="Photograph of a smiling mother lying beside her baby on soft white bedding"></div>
    <div class="cover__band cover__band--left"></div>
    <div class="cover__band cover__band--right"></div>

    <span class="glow glow--sun"></span>
    <span class="glow glow--coral"></span>

    <h1 class="title">
      <span class="title__kicker">THE CRADLE</span>
      <span class="title__hero">Compass</span>
      <span class="title__link">to Infancy's</span>
      <span class="title__closing"><span class="title__closing-main">Opening</span><span class="title__closing-tail">Seasons</span></span>
    </h1>

    <p class="subtitle">Grounded, Research-Led Methods on Rest, Nourishment, Protection plus Growing Assurance</p>

    <div class="topics">
      <div class="topic topic--safety" aria-label="Protection">
        <svg viewBox="0 0 28 28"><path d="M14 3 L23 6.5 V13 C23 19 19 23 14 25 C9 23 5 19 5 13 V6.5 Z"/><circle cx="14" cy="11" r="2.6"/><path d="M10.5 19 C11 15.5 17 15.5 17.5 19"/></svg>
      </div>
      <div class="topic topic--feeding" aria-label="Nourishment">
        <svg viewBox="0 0 28 28"><rect x="10" y="9" width="8" height="15" rx="2.5"/><path d="M11.5 9 V6.5 H16.5 V9"/><path d="M14 6.5 V3.5"/><path d="M10 14 H13 M10 18 H13"/></svg>
      </div>
      <div class="topic topic--sleep" aria-label="Rest">
        <svg viewBox="0 0 28 28"><path d="M17 4 A8 8 0 1 0 24 15 A6.5 6.5 0 0 1 17 4 Z"/><path d="M7 5 L7.8 7 L10 7.6 L7.8 8.3 L7 10.5 L6.2 8.3 L4 7.6 L6.2 7 Z"/></svg>
      </div>
    </div>
  </article>
</main>
</body>
</html>
```